Professional digital stationary

We need a digital stationary for our brand, we already have a logo and based on that we need a design for Word, Powerpoint, mailings and Linkedin. We need to be able to re use the stationary for other things like other social media. So basically what we ask is a template for Powerpoint and Word, some e-mail headers and a nice and professional Linkedin Header.

Target Market(s)

recruitment

Font styles to use
Sans Serif

```html
<!DOCTYPE html>
<html lang="en">
<head>
<meta charset="utf-8">
<title>Quorvane — LinkedIn header</title>
<link rel="stylesheet" href="https://fonts.googleapis.com/css2?family=Outfit:wght@200&display=swap">
<style>
  :root {
    --bg-top: #bdd784;
    --bg-mid: #a7c466;
    --bg-bottom: #92aa57;
    --edge-glow: rgba(255, 255, 255, 0.22);
    --text: #ffffff;
  }
  * { margin: 0; padding: 0; box-sizing: border-box; }
  html, body { width: 1200px; height: 469px; overflow: hidden; }
  body { font-family: "Outfit", sans-serif; }

  .header-banner {
    position: relative;
    width: 1200px;
    height: 469px;
    overflow: hidden;
    background: linear-gradient(180deg, var(--bg-top) 0%, var(--bg-mid) 35%, var(--bg-bottom) 100%);
  }
  .header-banner::before {
    content: "";
    position: absolute;
    inset: 0;
    background:
      linear-gradient(90deg, var(--edge-glow) 0, transparent 60px),
      linear-gradient(180deg, rgba(255,255,255,0.12) 0, transparent 32px);
    pointer-events: none;
  }

  .tagline {
    position: absolute;
    left: 377px;
    top: 208px;
    font-size: 37px;
    font-weight: 200;
    line-height: 1.2;
    letter-spacing: 0.5px;
    color: var(--text);
    white-space: nowrap;
  }

  .brand-name {
    position: absolute;
    left: 370px;
    top: 262px;
    font-size: 130px;
    font-weight: 200;
    line-height: 1.1;
    color: var(--text);
    white-space: nowrap;
  }
</style>
</head>
<body>
  <header class="header-banner">
    <p class="tagline">Smarter hiring, more freedom</p>
    <h1 class="brand-name">quorvane</h1>
  </header>
</body>
</html>
```